Stationery for Business and Financial Services Firm
Lantern Crest
Project: Stationery for Business and Financial Services Firm
Industry: Financial Services
Stationery for Business and Financial Services Firm - Financial Services
Creative Brief
Professional
Tobias Ferrand
Managing Director
P. O. Box 48307
Baraka Plaza, Suite # LVB-14,
Kilwa Orchard Road,
Dar-es-Salaam, Tanzania
tferrand@lanterncrest-example.co.tz
www.lanterncrest-example.co.tz
Lantern Crest (T) Ltd.
Wealth Management & Business Services
Address:
Baraka Plaza, Suite #LVB-14
Kilwa Orchard Road
Dar-es-Salaam
Tanzania
Tel: +255 22 2904417
Fax.: +255 22 2904418
Email: hello@lanterncrest-example.co.tz
Web: www.lanterncrest-example.co.tz
BUSINESS CARDS
Cell: +255 713 402 581
Email: tferrand@lanterncrest-example.co.tz
Services:
1.) Business Services
- Brand Management
- Business Valuation
- Capital & Debt Advisory
- Escrow Agents
2.) Wealth Management
- Business Succession
- Estate Planning
- Life Insurance
- Retirement Planning
- Savings & Investments
What I need:
1.) Letterhead
2.) Envelope
2.) Memo pad (A5 landscape)
3.) Business Card
Notes:
- The logo is the only finalized part of the branding, I am open to design suggestions for the rest. You can see how we are using it on the website (still under construction).
- I prefer modern fonts like Century Gothic, etc., so please suggest something on those lines.
- Look should be clean - befitting a financial adviser
- Card front and back
- The services also need to be listed on the stationery (if need be, at the back), as it will be part of the marketing of the company. The services are under two product lines, and individual services under each service line.
One suggestion (only suggestion, open to better ideas) would be to take two colors from the logo to represent two service lines, and leave the rest of the colors of the "lantern" for future use.
Hi All...
Seen a number of very good designs that I can work with - one bit of important detail:
The company name: Lantern Crest (T) Ltd. has to appear on all stationery, in slightly different way than rest of the address/contact details.
@farnolo: not a bad start... See project details... I need the services offered to be listed on all stationery, including the business cards, letterhead, envelope, and memo pad. Thanks.

```html
<!DOCTYPE html>
<html lang="en">
<head>
<meta charset="utf-8">
<title>Lantern Crest – Business Card</title>
<link rel="stylesheet" href="https://fonts.googleapis.com/css2?family=Didact+Gothic&display=swap">
<style>
  :root {
    --page-bg: #e9e7e4;
    --card-edge: #d9d9d9;
    --ink-grey: #58595b;
    --ink-soft: #6d6e70;
    --accent-purple: #7b2d86;
    --accent-orange: #f2922f;
    --accent-green: #8cc63f;
  }
  * { box-sizing: border-box; margin: 0; padding: 0; }
  html, body {
    width: 1200px;
    height: 913px;
    overflow: hidden;
    background: var(--page-bg);
    font-family: "Didact Gothic", "Century Gothic", sans-serif;
  }
  .business-card {
    position: absolute;
    left: 160px;
    top: 205px;
    width: 880px;
    height: 503px;
    background: radial-gradient(ellipse at 55% 45%, #ffffff 0%, #f7f7f7 70%, #f0f0f0 100%);
    border: 1px solid var(--card-edge);
    box-shadow: 0 12px 30px rgba(0,0,0,0.12);
  }
  .brand-name {
    position: absolute;
    left: 0; right: 0;
    top: 100px;
    text-align: center;
    font-size: 64px;
    line-height: 1;
    color: var(--ink-grey);
  }
  .company-name {
    position: absolute;
    left: 0; right: 0;
    top: 186px;
    text-align: center;
    font-size: 14px;
    letter-spacing: 3px;
    text-transform: uppercase;
    color: var(--ink-soft);
  }
  .person {
    position: absolute;
    left: 0; right: 0;
    top: 228px;
    text-align: center;
    font-size: 20px;
    color: var(--ink-soft);
  }
  .person-name { color: var(--accent-purple); }
  .person-divider { color: var(--accent-purple); margin: 0 8px; }
  .services {
    position: absolute;
    left: 0; right: 0;
    top: 290px;
    display: flex;
    flex-direction: column;
    align-items: center;
    gap: 8px;
    font-size: 12px;
    color: var(--ink-soft);
  }
  .service-line { white-space: nowrap; }
  .service-line-title { font-weight: normal; margin-right: 6px; }
  .service-line--business .service-line-title { color: var(--accent-orange); }
  .service-line--wealth .service-line-title { color: var(--accent-green); }
  .contacts {
    position: absolute;
    left: 0; right: 0;
    top: 392px;
    display: flex;
    flex-direction: column;
    align-items: center;
    gap: 10px;
    font-size: 13px;
    color: var(--ink-grey);
  }
  .contact-row {
    display: flex;
    align-items: center;
    gap: 16px;
    white-space: nowrap;
  }
  .contact-item {
    display: flex;
    align-items: center;
    gap: 5px;
  }
  .contact-icon { width: 13px; height: 13px; flex: none; }
</style>
</head>
<body>
  <main class="business-card">
    <h1 class="brand-name">Lantern Crest</h1>
    <p class="company-name">Lantern Crest (T) Ltd.</p>

    <p class="person">
      <span class="person-name">Tobias Ferrand</span><span class="person-divider">|</span><span class="person-title">Managing Director</span>
    </p>

    <div class="services">
      <p class="service-line service-line--business"><span class="service-line-title">Business Services:</span>Brand Management · Business Valuation · Capital &amp; Debt Advisory · Escrow Agents</p>
      <p class="service-line service-line--wealth"><span class="service-line-title">Wealth Management:</span>Business Succession · Estate Planning · Life Insurance · Retirement Planning · Savings &amp; Investments</p>
    </div>

    <div class="contacts">
      <div class="contact-row">
        <span class="contact-item">
          <svg class="contact-icon" viewBox="0 0 14 14" aria-hidden="true"><circle cx="7" cy="7" r="7" fill="#7b2d86"/><path d="M3.5 7.2 7 4l3.5 3.2H9.5V10h-5V7.2z" fill="#fff"/></svg>
          P. O. Box 48307 Baraka Plaza, Suite # LVB-14, Kilwa Orchard Road, Dar-es-Salaam, Tanzania
        </span>
        <span class="contact-item">
          <svg class="contact-icon" viewBox="0 0 14 14" aria-hidden="true"><circle cx="7" cy="7" r="7" fill="#7b2d86"/><circle cx="7" cy="7" r="3.6" fill="none" stroke="#fff" stroke-width="1"/><path d="M3.4 7h7.2M7 3.4v7.2" stroke="#fff" stroke-width="0.8"/></svg>
          www.lanterncrest-example.co.tz
        </span>
      </div>
      <div class="contact-row">
        <span class="contact-item">
          <svg class="contact-icon" viewBox="0 0 14 14" aria-hidden="true"><circle cx="7" cy="7" r="7" fill="#7b2d86"/><path d="M4.5 3.8c.6-.5 1.2-.4 1.5.2l.5 1c.2.4 0 .8-.3 1l-.4.3c.4.9 1 1.5 1.9 1.9l.3-.4c.2-.3.6-.5 1-.3l1 .5c.6.3.7.9.2 1.5-1.6 1.6-6.6-3.4-5.7-5.7z" fill="#fff"/></svg>
          255-22-290-4417
        </span>
        <span class="contact-item">
          <svg class="contact-icon" viewBox="0 0 14 14" aria-hidden="true"><circle cx="7" cy="7" r="7" fill="#7b2d86"/><rect x="5" y="3.2" width="4" height="7.6" rx="0.8" fill="#fff"/><rect x="5.6" y="4.2" width="2.8" height="4.8" fill="#7b2d86"/></svg>
          255-713-402-581
        </span>
        <span class="contact-item">
          <svg class="contact-icon" viewBox="0 0 14 14" aria-hidden="true"><circle cx="7" cy="7" r="7" fill="#7b2d86"/><rect x="4" y="6" width="6" height="4" rx="0.6" fill="#fff"/><rect x="5" y="3.6" width="4" height="2.6" fill="#fff"/></svg>
          255-22-290-4418
        </span>
        <span class="contact-item">
          <svg class="contact-icon" viewBox="0 0 14 14" aria-hidden="true"><circle cx="7" cy="7" r="7" fill="#7b2d86"/><rect x="3.6" y="4.6" width="6.8" height="4.8" fill="#fff"/><path d="M3.6 4.6 7 7.4l3.4-2.8" fill="none" stroke="#7b2d86" stroke-width="0.7"/></svg>
          tferrand@lanterncrest-example.co.tz
        </span>
      </div>
    </div>
  </main>
</body>
</html>
```